Real Estate Biz Card

-Card Size: Standard
-Background: Dark grey or black. I am open to gradient or a textured background.
-Other Colors: I dont mind pops of color. Contrasty blue, lime green, red Etc. Feel free to get creative.
-Text color: be creative
-Font: I like modern styles. Something that works well with my KV718 logo. See attached
-I would like my logo (KV718) watermarked on the card. Either on one side or both.
-Front of Card: keep it simple. Head shot, name, Logo, Phone #
-Back: add the rest of the details. See list below.
-brokerages logo as well as the Domivest and Equal Housing Opportunity logos on the card
-Name: Tod Marwick
-Residential Real Estate
-Cell:
-Email:
-Site:
-Office Address:
-very small/fine print "Each office independently owned & operated

```html
<!DOCTYPE html>
<html lang="en">
<head>
<meta charset="utf-8">
<title>KV718 Business Card – Tod Marwick</title>
<link rel="stylesheet" href="https://fonts.googleapis.com/css2?family=Exo+2:wght@500;600;700&family=Roboto:wght@400;500&display=swap">
<style>
  :root {
    --backdrop: #2a2a2a;
    --brand-red: #ff0000;
    --band-grey: #7f7f7f;
    --card-front: #f1f1f1;
    --card-back-top: #a6a6a6;
    --card-back-bottom: #7b7b7b;
    --text-white: #ffffff;
    --tagline-grey: #8a8a8a;
    --photo-top: #c9ccd3;
    --photo-bottom: #4d6391;
  }
  * { margin: 0; padding: 0; box-sizing: border-box; }
  html, body { width: 1200px; height: 960px; overflow: hidden; }
  body { background: var(--backdrop); position: relative; font-family: "Roboto", Arial, sans-serif; }

  .card { position: absolute; width: 600px; height: 342px; overflow: hidden; }
  .card-front { left: 302px; top: 129px; background: var(--card-front); }
  .card-back { left: 299px; top: 488px; background: linear-gradient(180deg, var(--card-back-top), var(--card-back-bottom)); }

  .front-bands { position: absolute; left: 0; top: 0; }

  .agent-info {
    position: absolute; right: 33px; top: 13px; text-align: right;
    font-family: "Exo 2", Arial, sans-serif; color: var(--text-white); line-height: 1.2;
  }
  .agent-name { font-size: 21px; font-weight: 600; letter-spacing: 0.5px; }
  .agent-role, .agent-phone { font-size: 13.5px; font-weight: 500; letter-spacing: 0.6px; }

  .headshot {
    position: absolute; left: 0; top: 52px; width: 298px; height: 290px;
    background: linear-gradient(180deg, var(--photo-top) 0%, var(--photo-bottom) 70%);
  }

  .brand-front { position: absolute; left: 310px; top: 160px; width: 260px; text-align: center; }
  .brand-name {
    font-family: "Exo 2", Arial, sans-serif; font-weight: 700;
    font-size: 64px; line-height: 1; color: var(--brand-red); letter-spacing: 1px;
  }
  .brand-tagline {
    margin-top: 6px; font-family: "Exo 2", Arial, sans-serif; font-size: 10px; font-weight: 500;
    letter-spacing: 4.2px; color: var(--tagline-grey); text-transform: uppercase;
  }

  .contact-block { position: absolute; left: 70px; top: 86px; color: var(--text-white); }
  .address { font-size: 14.5px; line-height: 18px; }
  .contact-list { list-style: none; margin-top: 9px; font-size: 14.5px; line-height: 18px; }
  .contact-list li { display: flex; align-items: center; gap: 8px; }
  .contact-list svg { width: 13px; height: 13px; fill: var(--text-white); }
  .fine-print { margin-top: 10px; font-size: 8.5px; }
  .affiliations { display: flex; align-items: center; gap: 6px; margin-top: 12px; }
  .badge { width: 18px; height: 20px; background: var(--text-white); }
  .brokerage { margin-left: 4px; font-size: 13px; font-weight: 500; color: var(--text-white); }

  .brand-back {
    position: absolute; left: 316px; top: 186px;
    font-family: "Exo 2", Arial, sans-serif; font-weight: 700;
    font-size: 54px; line-height: 1; color: var(--text-white); letter-spacing: 1px;
  }
</style>
</head>
<body>

  <section class="card card-front">
    <svg class="front-bands" width="600" height="90" viewBox="0 0 600 90" aria-hidden="true">
      <rect x="0" y="0" width="600" height="14" fill="var(--brand-red)"/>
      <polygon points="0,18 288,18 310,39 0,39" fill="var(--band-grey)"/>
      <polygon points="288,14 600,0 600,81 362,81 296,14" fill="var(--brand-red)"/>
      <polygon points="386,0 600,0 600,81 362,81 290,14 386,14" fill="var(--brand-red)"/>
    </svg>

    <div class="agent-info">
      <p class="agent-name">TOD MARWICK</p>
      <p class="agent-role">Residential Real Estate</p>
      <p class="agent-phone">555 214 7093</p>
    </div>

    <div class="headshot" role="img" aria-label="Headshot portrait of the agent"></div>

    <div class="brand-front">
      <p class="brand-name">KV718</p>
      <p class="brand-tagline">Real Estate in the 718</p>
    </div>
  </section>

  <section class="card card-back">
    <div class="contact-block">
      <p class="address">4120 Alder Ridge Way<br>Fairbanks, Alaska 99012</p>
      <ul class="contact-list">
        <li>
          <svg viewBox="0 0 24 24" aria-hidden="true"><path d="M6.6 10.8a15.2 15.2 0 0 0 6.6 6.6l2.2-2.2a1 1 0 0 1 1-.25 11.4 11.4 0 0 0 3.6.57 1 1 0 0 1 1 1V20a1 1 0 0 1-1 1A17 17 0 0 1 3 4a1 1 0 0 1 1-1h3.5a1 1 0 0 1 1 1c0 1.25.2 2.45.57 3.57a1 1 0 0 1-.25 1z"/></svg>
          555 380 6172
        </li>
        <li>
          <svg viewBox="0 0 24 24" aria-hidden="true"><path d="M2 5h20v14H2z M2 5l10 8 10-8" fill="none" stroke="#fff" stroke-width="2"/></svg>
          tod@kv718.com
        </li>
        <li>
          <svg viewBox="0 0 24 24" aria-hidden="true"><circle cx="12" cy="12" r="10"/></svg>
          www.kv718.com
        </li>
      </ul>
      <p class="fine-print">Each office independently owned &amp; operated</p>
      <div class="affiliations">
        <span class="badge" role="img" aria-label="Domivest member badge"></span>
        <span class="badge" role="img" aria-label="Equal housing opportunity badge"></span>
        <span class="brokerage">Northgate Realty</span>
      </div>
    </div>

    <p class="brand-back">KV718</p>
  </section>

</body>
</html>
```